Wordpress-Design für das neue Kinder- und Jugendforum der Stadt Nordhaven
Zielgruppe
Kinder- und Jugendforum der Stadt Nordhaven:
Das KOMPA. ist eine kommunale Einrichtung der Stadtjugendpflege, ein offenes Haus für alle Kinder in und um Husum (liegt direkt an der Nordsee).
Zielgruppe ist die Altersgruppe zwischen 10 und 20 Jahren (und deren Eltern).
Allerdings sind wir mitten im Zentrum. Etwas Seriosität ist durchaus erwünscht. Nachbar links: VitaPunkt, Nachbar rechts: Greta Wollin und wir mittendrin ;)
Aufgabenstellung
Nach dem großen Erfolg unseres ersten Projektes auf dieser Plattform mit 348 Designvorschlägen möchten wir heute gerne auch unser Wordpress-Design ausschreiben:
Für das im neuen Jahr zu eröffnende "Kinder- und Jugendforum der Stadt Nordhaven" suchen wir, das Treffpunkt Nord in Husum, heute über diese Plattform ein Wordpress-Design.
Unser Logo haben wir bereits in unserem Projekt
https://www.grafikwettbewerb.de/208716-logo-fuer-das-neue-kinder-und-jugendforum-der-stadt-husum
gefunden. Das Logo muss also in das neue Design eingebunden werden bzw. das Design sollte zum neuen Logo passen (ggf. auch von der Farbgebung). Wir haben das Logo als .png-Datei an das Projekt angehangen.
Wir werden Insgesamt ca. 10-12 verschiedene (Unter)Seiten benötigen, daher auch das erhöhte Preisgeld. Das Design der einzelnen Unterseiten wird sich nicht groß von den anderen Seiten unterschieden (müssen).
Folgende Elemente (= Menüstruktur) sollten in der fertigen Wordpress-Installation (auf unserem Server) auf jeden Fall vom Design her enthalten sein. Wir haben die Liste hier so aufgeführt, wie das Hauptmenü mit seinen Untermenüpunkten am Ende auf der Seite erscheinen soll. Das Hauptmenü (oben?) muss nicht sehr auffällig sein, da wir (siehe unten) eine Art grafisches Menü auf der Startseite wünschen:
- Startseite
- DAS KOMPA
--- Jungnetz
--- Bundesstiftung Kinderhilfe
--- Offene Ganztagsschule
--- Pfadfinder
--- Webcams
- Veranstaltungen
--- Kindertheater
--- Sommerkarte
--- Sternfestival
- Kontaktformular (mit Captcha)
- Impressum
Erklärungen zu den einzelnen Punkten:
Startseite: Hier sollen, wie auf unserer derzeitigen Seite, oben GROSS unsere "Neuesten Artikel" gelistet werden. Wir stellen uns das so vor: Oben werden große "Newsbilder" aus den X neuesten Artikeln, die wir veröffentlichen, mit samt des "..

```html
<!DOCTYPE html>
<html lang="de">
<head>
<meta charset="utf-8">
<title>KOMPA – Kinder- und Jugendforum</title>
<link href="https://fonts.googleapis.com/css2?family=Barlow:wght@400;500;600&display=swap" rel="stylesheet">
<style>
:root{
  --brand:#a3262b;
  --ink:#2b2b2b;
  --red-1:#7a1511;--red-2:#a8232a;--red-3:#d22a2f;--red-4:#e8322a;
  --rose-1:#8f4c4b;--rose-2:#b8434a;--rose-3:#dc5a5e;--rose-4:#ef665c;
  --orange:#e3832a;--amber:#f4a533;
  --navy:#12113f;
  --row-1:#282a5a;--row-2:#3d3e6b;--row-3:#5a5a7f;--row-4:#6f6f95;--row-5:#8a8ba9;
  --teal-1:#63c4b0;--teal-2:#4fbaa1;--teal-3:#33ae93;
  --white:#fff;
}
*{margin:0;padding:0;box-sizing:border-box}
html,body{width:1200px;height:1187px;overflow:hidden}
body{font-family:"Barlow",sans-serif;color:var(--white);background:var(--white);position:relative}
.site-header{position:absolute;left:0;top:0;width:1200px;height:89px;background:var(--white)}
.brand{position:absolute;left:80px;top:14px;color:var(--brand);font-weight:600;font-size:50px;line-height:1;letter-spacing:1px}
.brand-sub{position:absolute;left:81px;top:64px;color:var(--brand);font-size:7px}
.main-nav{position:absolute;left:346px;top:42px;display:flex;gap:27px}
.main-nav a{color:#333;font-weight:600;font-size:16px;text-decoration:none}
.header-icons{position:absolute;right:80px;top:43px;display:flex;gap:25px}
.header-icons svg{width:18px;height:18px}
.hero{position:absolute;left:0;top:89px;width:1200px;height:431px;background:linear-gradient(100deg,#6b3a2c 0%,#9b6a55 30%,#b5876c 50%,#8a5c47 75%,#4c2c22 100%)}
.hero-meta{position:absolute;left:78px;top:66px;background:var(--white);color:var(--ink);font-size:16px;padding:7px 13px;height:32px}
.hero-title{position:absolute;left:78px;top:97px;background:var(--white);color:#111;font-weight:600;font-size:32px;height:52px;padding:6px 13px;letter-spacing:.5px}
.teaser{position:absolute;left:968px;width:151px;height:91px;border:3px solid var(--white);background:var(--white)}
.teaser span{position:absolute;left:6px;top:3px;font-size:10px;color:var(--ink);background:var(--white);padding:0 2px}
.teaser .pic{position:absolute;left:3px;top:3px;right:3px;bottom:3px}
.tile-grid{position:absolute;left:0;top:520px;width:1200px}
.tile-row{display:flex;height:45px}
.tile-row a{display:flex;align-items:center;justify-content:center;color:var(--white);text-decoration:none;font-size:16px;font-weight:500;letter-spacing:.3px}
.c1{width:346px}.c2{width:267px}.c3{width:266px}.c4{width:321px}
.media{position:absolute;left:0;top:609px;width:1200px;height:89px;display:flex}
.media a{display:flex;align-items:center;justify-content:center;gap:10px;color:var(--white);text-decoration:none;font-size:32px;font-weight:500}
.today-head{position:absolute;left:0;top:698px;width:1200px;height:89px;background:var(--navy)}
.today-head h2{position:absolute;width:100%;text-align:center;top:26px;font-size:32px;font-weight:600;letter-spacing:.5px}
.today-head a{position:absolute;right:80px;top:36px;color:var(--white);text-decoration:none;font-size:16px;font-weight:500;display:flex;gap:5px;align-items:center}
.schedule{position:absolute;left:0;top:787px;width:1200px;list-style:none}
.schedule li{height:44.4px;display:flex;align-items:center;font-size:15.5px;border-top:1px dotted rgba(255,255,255,.35);letter-spacing:.3px}
.schedule time{width:258px;padding-left:81px}
.site-footer{position:absolute;left:0;top:1009px;width:1200px;height:178px}
.band{height:44.5px}
.footer-main{position:absolute;left:0;top:89px;width:1200px;height:89px;background:var(--teal-3)}
.partner{position:absolute;top:37px;font-size:15px;font-weight:600;color:var(--white)}
.footer-links{position:absolute;right:80px;top:37px;display:flex;gap:27px}
.footer-links a{color:var(--white);text-decoration:none;font-size:16px;font-weight:500}
</style>
</head>
<body>
<header class="site-header">
  <div class="brand">KOMPA</div>
  <div class="brand-sub">Kinder- und Jugendforum der Stadt Nordhaven</div>
  <nav class="main-nav"><a href="#">DAS KOMPA</a><a href="#">VERANSTALTUNGEN</a><a href="#">NEWS</a></nav>
  <div class="header-icons">
    <svg viewBox="0 0 18 18"><circle cx="7.5" cy="7.5" r="5" fill="none" stroke="#333" stroke-width="2.4"/><line x1="11" y1="11" x2="16" y2="16" stroke="#333" stroke-width="2.6"/></svg>
    <svg viewBox="0 0 18 18"><path d="M9 1a5 5 0 0 0-5 5c0 4 5 11 5 11s5-7 5-11a5 5 0 0 0-5-5z" fill="#333"/><circle cx="9" cy="6" r="2" fill="#fff"/></svg>
    <svg viewBox="0 0 18 18"><rect x="1.5" y="4" width="15" height="11" fill="none" stroke="#333" stroke-width="1.8"/><path d="M1.5 4l7.5 6 7.5-6" fill="none" stroke="#333" stroke-width="1.8"/></svg>
  </div>
</header>

<section class="hero" role="img" aria-label="Foto einer Band beim Wohnzimmerkonzert auf der Bühne">
  <div class="hero-meta">Veranstaltungen | 22. März 2013</div>
  <div class="hero-title">WOHNZIMMERKONZERT</div>
  <div class="teaser" style="top:34px"><div class="pic" role="img" aria-label="Foto vom Wohnzimmerkonzert" style="background:linear-gradient(90deg,#4a3a32,#9a7a66,#3a302c)"></div><span>WOHNZIMMERKONZERT</span></div>
  <div class="teaser" style="top:171px"><div class="pic" role="img" aria-label="Foto von der Ferienparty" style="background:linear-gradient(90deg,#7a5a6a,#c98aa0,#d0465a)"></div><span>FERIENPARTY</span></div>
  <div class="teaser" style="top:308px"><div class="pic" role="img" aria-label="Foto vom Kindertheater" style="background:linear-gradient(90deg,#c9b36a,#3c3a3a,#f0a020)"></div><span>KINDERTHEATER</span></div>
</section>

<nav class="tile-grid">
  <div class="tile-row">
    <a class="c1" href="#" style="background:var(--red-1)">JUNGNETZ</a>
    <a class="c2" href="#" style="background:var(--red-2)">BUNDESSTIFTUNG KINDERHILFE</a>
    <a class="c3" href="#" style="background:var(--red-3)">OFFENE GANZTAGSSCHULE</a>
    <a class="c4" href="#" style="background:var(--red-4)">PFADFINDER</a>
  </div>
  <div class="tile-row">
    <a class="c1" href="#" style="background:var(--rose-1)">KINDERTHEATER</a>
    <a class="c2" href="#" style="background:var(--rose-2)">SOMMERKARTE</a>
    <a class="c3" href="#" style="background:var(--rose-3)">STERNFESTIVAL</a>
    <a class="c4" href="#" style="background:var(--rose-4)">TERMINE</a>
  </div>
</nav>

<div class="media">
  <a href="#" style="width:613px;background:var(--orange)">
    <svg width="36" height="24" viewBox="0 0 36 24"><rect x="0" y="2" width="24" height="20" rx="4" fill="#fff"/><path d="M25 12l11-9v18z" fill="#fff"/></svg>WEBCAM</a>
  <a href="#" style="width:587px;background:var(--amber)">
    <svg width="34" height="30" viewBox="0 0 34 30"><path d="M4 6h7l3-5h6l3 5h7a4 4 0 0 1 4 4v16a4 4 0 0 1-4 4H4a4 4 0 0 1-4-4V10a4 4 0 0 1 4-4z" fill="#fff"/><circle cx="17" cy="17" r="7" fill="var(--amber)"/><circle cx="17" cy="17" r="4" fill="#fff"/></svg>FOTOS</a>
</div>

<section class="today-head">
  <h2>HEUTE IM KOMPA</h2>
  <a href="#"><svg width="16" height="16" viewBox="0 0 16 16"><rect x="1" y="3" width="14" height="12" fill="none" stroke="#fff" stroke-width="1.5"/><line x1="1" y1="7" x2="15" y2="7" stroke="#fff" stroke-width="1.5"/><line x1="5" y1="1" x2="5" y2="4" stroke="#fff" stroke-width="1.5"/><line x1="11" y1="1" x2="11" y2="4" stroke="#fff" stroke-width="1.5"/></svg>MONATSÜBERSICHT</a>
</section>

<ul class="schedule">
  <li style="background:var(--row-1)"><time>13.00 Uhr</time>KOMPA: Die Jugendinfo im TPN hat geöffnet! Beraten, Informieren, Snacken &amp; Spielen</li>
  <li style="background:var(--row-2)"><time>13.00 Uhr</time>Pfadfindergruppe „Jakob Lindqvist“</li>
  <li style="background:var(--row-3)"><time>14.30 Uhr</time>Kindertöpfern mit Marlene</li>
  <li style="background:var(--row-4)"><time>15.30 Uhr</time>Im „WERK“ wird gewerkelt. Heute für Jungen!</li>
  <li style="background:var(--row-5)"><time>17.00 Uhr</time>Basketball ab 14 Jahren</li>
</ul>

<footer class="site-footer">
  <div class="band" style="background:var(--teal-1)"></div>
  <div class="band" style="background:var(--teal-2)"></div>
  <div class="footer-main">
    <span class="partner" style="left:80px">Bundesstiftung Kinderhilfe</span>
    <span class="partner" style="left:280px">Jungnetz</span>
    <nav class="footer-links"><a href="#">KONTAKT</a><a href="#">IMPRESSUM</a></nav>
  </div>
</footer>
</body>
</html>
```